Flyer-Design für Segelverein
Zielgruppe
Wir sind ein kleiner Berliner Segelverein im Herzen von Berlin. Unsere Zielgruppe sind wasserbegeisterte Menschen zwischen 20-50 Jahre.
Ein Eindruck über unseren Verein gibt es auf der neuen Webseite (noch im Aufbau): www.wellenrunde-kiel.de
und der alten webseite: www.wellenrundekiel.de
Aufgabenstellung
Wir benötigen den Flyer zum Anwerben neuer Mitglieder. D.h. der Flyer soll alle notwendigen Informationen beinhalten, auf das nötigste reduziert. Vom Format würden wir daher eher was kompaktes sehen (z.b. DIN lang beidseitig bedruckt). Dann könnte auf der Vorderseite die wichtigsten Informationen zum Verein stehen und auf der Rückseite Gründe, Mitglied zu werden.
Zum Verein
1972 gegründet mit dem Ziel, das Seesegeln zu fördern. Die damalige Begeisterung, gemeinsam etwas vollbringen zu können, führte in den Jahren 1975/76 zu einer Folge von Seetörns, bei der ausnahmslos Mitglieder beteiligt waren, von der Ostsee über Norwegen, England, Kanarische Inseln, Karibik über die Bermudas und Azoren wieder zurück in die Ostsee.
Warum der Verein:
- Verkehrsgünstig und zentral gelegen direkt an der Lindgasse - Sehr gut zu erreichen mit den ÖPNVs
- Einzigartiger Schwimmsteg in Berlin ohne Landzugang - Ein Ort zum Verweilen und Abschalten
- verfügbare Stegplätze für Bootsbesitzer
- Viele Vereinsboote für Mitglieder ohne Boot -
- Günstige Mitgliedsbeiträge - Studenten und Schüler erhalten Ermässigungen
- Ein familiärer kleiner Verein - Keine umfangreichen Pflichtarbeiten
- Vereinsinterne Regatten entlang der Havel
- Spannende interne Events und Ausbildungsangebote wie z.b. Fahrten mit dem Dreimast-Gaffelschooner Solvenja, Knotenkurse, Navigation

```html
<!DOCTYPE html>
<html lang="de">
<head>
<meta charset="utf-8">
<title>Wellenrunde KIEL – Mitgliederflyer</title>
<link rel="stylesheet" href="https://fonts.googleapis.com/css2?family=Lexend+Exa:wght@400;500&family=Lexend:wght@300;400&display=swap">
<style>
  :root {
    --stage: #e9e8e6;
    --white: #ffffff;
    --signal-red: #e3262b;
    --club-blue: #0e5299;
    --deep-navy: #173a6d;
    --lake-blue: #b8d9f2;
    --sky-grey: #c9ccd2;
    --deck-dark: #2b2c31;
    --water-light: #d7e6ef;
    --water-deep: #4d7d99;
  }
  * { margin: 0; padding: 0; box-sizing: border-box; }
  html, body { width: 1200px; height: 672px; overflow: hidden; background: var(--stage); }
  .stage {
    width: 1200px; height: 672px;
    display: flex; align-items: center; justify-content: center; gap: 24px;
  }
  .flyer {
    position: relative; width: 572px; height: 300px; overflow: hidden;
    box-shadow: 0 6px 18px rgba(0,0,0,.18);
    font-family: "Lexend", sans-serif; color: var(--white);
  }

  /* Vorderseite */
  .front-photo {
    position: absolute; inset: 0;
    background: linear-gradient(170deg, var(--sky-grey) 0%, #8a8d95 38%, #4a4b52 60%, var(--deck-dark) 100%);
  }
  .club-mark {
    position: absolute; top: 24px; right: 26px;
    display: flex; align-items: center; gap: 8px;
    font-family: "Lexend Exa", sans-serif; font-size: 14px; font-weight: 500;
  }
  .club-mark .dot { width: 22px; height: 22px; border-radius: 50%; background: var(--signal-red); }
  .front-claim {
    position: absolute; right: 26px; bottom: 40px; text-align: right;
  }
  .front-claim h1 {
    font-family: "Lexend Exa", sans-serif; font-weight: 400; font-size: 27px; letter-spacing: .5px; line-height: 1.1;
  }
  .front-claim p { font-size: 11.5px; margin-top: 4px; }

  /* Rückseite */
  .back-shapes { position: absolute; inset: 0; }
  .back-headline {
    position: absolute; left: 150px; top: 14px;
    font-family: "Lexend Exa", sans-serif; font-size: 25px; font-weight: 400;
  }
  .back-call {
    position: absolute; left: 150px; top: 50px;
    font-family: "Lexend Exa", sans-serif; font-size: 17px; color: var(--signal-red);
  }
  .back-info { position: absolute; left: 112px; top: 92px; }
  .back-info h2 {
    font-family: "Lexend Exa", sans-serif; font-size: 13px; font-weight: 500; letter-spacing: .5px; margin-bottom: 4px;
  }
  .reasons { list-style: none; font-size: 9.6px; line-height: 1.38; }
  .reasons li::before { content: "- "; }
  .contact {
    position: absolute; left: 92px; bottom: 14px;
    font-size: 7.8px; font-weight: 300; line-height: 1.35;
  }
  .map-area {
    position: absolute; right: 118px; bottom: 14px; width: 128px; height: 84px;
    background: linear-gradient(160deg, var(--lake-blue), #9cc6e6); border-radius: 6px;
  }
</style>
</head>
<body>
<main class="stage">

  <section class="flyer flyer-front">
    <div class="front-photo" role="img" aria-label="Foto: Blick über das Deck einer Segelyacht mit Winsch und Segel auf glitzerndes Wasser"></div>
    <div class="club-mark"><span class="dot"></span>Wellenrunde</div>
    <div class="front-claim">
      <h1>Seemann lass das Träumen</h1>
      <p>Wellenrunde KIEL - der Segelverein im Herzen von Kiel</p>
    </div>
  </section>

  <section class="flyer flyer-back">
    <svg class="back-shapes" width="572" height="300" viewBox="0 0 572 300" aria-hidden="false">
      <defs>
        <linearGradient id="water" x1="0" y1="0" x2="1" y2="1">
          <stop offset="0" stop-color="var(--water-light)"/>
          <stop offset=".55" stop-color="var(--water-deep)"/>
          <stop offset="1" stop-color="var(--water-light)"/>
        </linearGradient>
      </defs>
      <rect width="572" height="300" fill="url(#water)" role="img" aria-label="Foto: aufspritzendes Wasser in Nahaufnahme"/>
      <path d="M125 0 H535 Q575 150 510 300 H40 Q70 140 125 0 Z" fill="#e4ecf2"/>
      <path d="M135 0 H520 Q558 150 495 300 H52 Q82 140 135 0 Z" fill="var(--club-blue)"/>
      <path d="M70 300 Q85 170 108 86 Q300 70 480 110 Q505 210 468 300 Z" fill="var(--deep-navy)"/>
    </svg>

    <div class="back-headline">Klar zum Ablegen!</div>
    <div class="back-call">Jetzt Mitglied werden!</div>

    <div class="back-info">
      <h2>Wellenrunde KIEL</h2>
      <ul class="reasons">
        <li>Verkehrsgünstig und zentral gelegen</li>
        <li>einzigartiger Schwimmsteg ohne Landzugang</li>
        <li>Stegplätze für Bootsbesitzer verfügbar</li>
        <li>viele Vereinsboote</li>
        <li>günstige Mitgliedsbeiträge</li>
        <li>kleiner familiärer Verein</li>
        <li>vereinsinterne Regatten</li>
        <li>Events und Ausbildungsangebote</li>
      </ul>
    </div>

    <div class="contact">
      Am Lindensee 4, 24103 Kiel<br>
      info@wellenrunde-kiel.de<br>
      www.wellenrundekiel.de<br>
      +49 (0431) 555 01 23
    </div>

    <div class="map-area" role="img" aria-label="Lageplan: See mit Vereinsgelände an der Lindgasse, Standort markiert"></div>
  </section>

</main>
</body>
</html>
```